Talent Management Company Needs Business Cards

Using one of the logos provided (attached) K&R Talent Collective needs a business card designed.
Please visit our website for more information about us-

www.krtalentcollective.example

The face should feature a dramatic presentation of the logo with the back being reserved for our professional information which is:

The information should be:
Dorian T. Vickers
C.E.O
Email: dtvickers@krtalentcollective.example
Mobile: 555-804-2917
Website: www.krtalentcollective.example

Marcus L. Vickers
Director of Public Relations
Email: mlvickers@krtalentcollective.example
Mobile: 555-806-3350

Jules R. Hampton
Director of Client Development
Email: jhampton@krtalentcollective.example

Simon Hurlock
Director of Brand Development
Email: shurlock@krtalentcollective.example

Would like the logo to have color. I would like to see one side red or black and the other side white but if it looks better in either black or red that would be fine to but would like to see how it comes out.

Please feel free to message me and if you would like just the icon alone I have other image files that I can send as well.

Target Market(s)

Professional Athletes, coaches, entertainers age 18-35 but also must be accepted in the business community

Industry/Entity Type

Business

Requirements
Must have
• 1) Use the logo
2) Double sided
3) Distinctive
Nice to have
• Small simple images for telephone, e-mail, and Url.

```html
<!DOCTYPE html>
<html lang="en">
<head>
<meta charset="utf-8">
<title>K&amp;R Talent Collective — Business Card</title>
<link rel="stylesheet" href="https://fonts.googleapis.com/css2?family=Jost:ital,wght@0,400;0,500;1,400&display=swap">
<style>
  :root {
    --page: #ffffff;
    --red-bright: #e3151f;
    --red-mid: #c40c16;
    --red-deep: #6e0007;
    --accent: #e0161f;
    --ink: #111111;
    --text: #3b3b3b;
    --frame: #8a8a8a;
  }
  * { margin: 0; padding: 0; box-sizing: border-box; }
  html, body {
    width: 1200px; height: 926px; overflow: hidden;
    background: var(--page);
    font-family: "Jost", "Futura", sans-serif;
  }
  .canvas { position: relative; width: 1200px; height: 926px; }

  .card { position: absolute; top: 97px; width: 472px; height: 730px; overflow: hidden; }

  .card--front { left: 116px; }
  .front-field {
    position: absolute; inset: 0;
    background:
      radial-gradient(ellipse 120% 90% at 30% 10%, var(--red-bright) 0%, var(--red-mid) 45%, var(--red-deep) 100%);
  }
  .front-name {
    position: absolute; top: 118px; right: 32px;
    color: #ffffff; font-weight: 500; font-size: 26px;
    letter-spacing: 0.5px;
  }

  .card--back {
    left: 625px;
    border: 1.5px solid var(--frame);
    background: #ffffff;
  }
  .wordmark {
    position: absolute; top: 242px; left: 54px; right: 20px;
    color: var(--ink); font-weight: 500; font-size: 28px; line-height: 34px;
    letter-spacing: 0.2px; text-transform: uppercase; white-space: nowrap;
  }
  .holder { position: absolute; top: 387px; left: 54px; color: var(--text); }
  .holder__name { font-size: 22px; font-weight: 500; letter-spacing: 0.6px; line-height: 28px; }
  .holder__title { font-size: 21px; font-style: italic; line-height: 28px; }

  .contact { position: absolute; top: 485px; left: 54px; list-style: none; color: var(--text); font-size: 19px; line-height: 27px; white-space: nowrap; }
  .contact__label { color: var(--accent); font-weight: 500; display: inline-block; width: 28px; }

  .address { position: absolute; top: 602px; left: 54px; color: var(--text); font-size: 19px; line-height: 25px; font-style: normal; }

  .side-label {
    position: absolute; top: 848px; width: 472px; text-align: center;
    font-size: 34px; font-weight: 500; color: #000;
  }
  .side-label--front { left: 116px; }
  .side-label--back { left: 625px; }
</style>
</head>
<body>
<main class="canvas">
  <section class="card card--front">
    <div class="front-field" role="img" aria-label="Red gradient field with a faint repeating star pattern"></div>
    <p class="front-name">K&amp;R Talent Collective</p>
  </section>

  <section class="card card--back">
    <p class="wordmark">K&amp;R Talent Collective</p>
    <div class="holder">
      <p class="holder__name">Dorian T. Vickers</p>
      <p class="holder__title">CEO</p>
    </div>
    <ul class="contact">
      <li><span class="contact__label">T :</span> 555-804-2917</li>
      <li><span class="contact__label">E :</span> dtvickers@krtalentcollective.example</li>
      <li><span class="contact__label">W:</span> www.krtalentcollective.example</li>
    </ul>
    <address class="address">1820 Harbor View Rd<br>Suite 410, Lakeport, OH 45000</address>
  </section>

  <p class="side-label side-label--front">Front</p>
  <p class="side-label side-label--back">Back</p>
</main>
</body>
</html>
```